依頼詳細
【コンテンツ】
基本的なコンテンツは、現在のページ https://korvane.jp/ を元に構成してください。
・[制作実績] ですが、[制作実績 - ホームページ] と [制作実績 - システム開発] に分けて頂き、それぞれ簡単な説明テキスト「○○○…」とイメージ画像などがあると良いかもしれません(ブロック内の正方形のサンプル画像はそのままご使用頂いても [No Photo] 等で代替して頂いても結構です)。
・[お知らせ] と [お問い合わせはこちら] の間に [よくあるご質問] のブロックを追加してください(テキストは「○○○…」で結構です)。
・その他、企業サイトによくあるようなコンテンツで おすすめのコンテンツがございましたら デザイン内にてご提案頂けますと幸いです。

【レイアウト】
・レイアウトは(現状2カラムになってますが)1カラムで構成して頂いても結構です。おすすめのレイアウトでお願いいたします(バナー広告は不要です)。
・幅は1366pxでお願いいたします(最近見かけます画面一杯に広がっているレイアウトはあまり好みではありません。背景画像が画面一杯に広がっているのは構いませんが、コンテンツは中央よりに配置したいと思います。後ほど弊社にてレスポンシブにコーディングする予定です)。
・グローバルメニューは現状の6メニューでお願いいたします。フッターメニューは常時差し替えが発生しますので「○○○」などで代替して頂いて結構です。

【配色・デザイン等】
・配色としては モノトーン(黒)を基調として頂き、見出し背景色などもモノトーンでも結構ですし、あえて一色挙げるとしますと #405080 (HSV 225度 - 50% -50%) などのネイビーまたは青などのクールな色味が好みです。その他のアイキャッチ画像やコンテンツ等の色味は単色でもカラフルなものでも結構です。ブリッカー様のセンスにお任せしたいと思います。
・ロゴマークは先日 Brikka で依頼したものですので、変更せずにそのままご使用ください。
・アイキャッチ等の写真画像は、弊社で Pelmora Images をライセンス契約しておりますので、Pelmora Images のサンプル画像をご使用頂き、別途 画像のURLを当選後にお知らせ頂けましたら結構です。
・アイキャッチ画像のイメージ(内容)ですが、弊社のサービスは 主軸サービス(バックエンド)として (1)システム開発 があり、集客用サービス(フロントエンド)として (2)ホームページ制作 があります。これらのサービスを総合すると (1) を構成する お客様の「笑顔」と弊社の「誠実さ」との「信頼関係」(人間性)がベースとなり、その上に (2) のホームページ制作(デジタルITサービス)が存在する…といったイメージになると思います。それら2つを、例えば半透明にして手前と奥で重ね合わせる/上下にレイアウトする/2枚の画像を JavaScript でアニメーション化するなどは、ブリッカー様のセンスにてお願いできましたらと思います(弊社にてコーディングしますのでご提案ください)。
サイトURL
https://korvane.jp/
ページ数
1ページ
希望イメージ
シンプル 複雑
単色 カラフル
暗い 明るい
日常 高級
遊び心 厳粛
未来的 伝統的
女性的 男性的
希望する色
青系、水色系、グレー系
納品ファイル
• フォトショップ形式 (.psd)
補足説明
Adobe Photoshop CC *psd 形式で、レイヤーを分けて制作・納品頂けますと幸いです。
予想していたよりも提案件数が少なかったので、少し内容をシンプルにして 期間を延長させて頂きました。変更箇所とその他印象等は 以下の通りでございますので、何卒よろしくお願い申し上げます。

【依頼詳細の変更】
・アイキャッチ画像のイメージ(内容)ですが「パソコンで仕事をしている人の笑顔」が含まれている画像でしたらどんなものでも結構です。(すでにご提案頂いているものにつきましては修正して頂かなくても結構です)
・「How to enjoy creative work?」というテキストは入れて頂かない方が良いかと思います(そこまで重要視しておりませんので)。
・見出しテキスト(「制作実績」「お知らせ」など)は左寄せの方が好みです。
・全体の配色ですが、カラフルな感じより 白を基調としたモノトーンな感じの方が好みです。
・[お問い合わせはこちら] ですが、今後 他のページ(ランディングページ)などにも挿入していく可能性がありますので、バナーっぽく制作頂けますと有り難いです。

白を基調としたシンプルなレイアウトで、ディテールまで洗練されていたデザインでしたので 一目見て気に入って選ばせて頂きました。
テンプレートでのデザインが主流になりつつある中、テンプレートでは表現できないような個性のあるものになったのではないかと思いまして 大変満足しております。ありがとうございました。

皆様に個別に御礼メッセージをお送りすることはできませんでしたが、予想以上の大変多くのご提案をご応募頂けまして大変満足しております。本当にありがとうございました。また機会がございましたら 何卒よろしくお願い申し上げます。

```html
<!DOCTYPE html>
<html lang="ja">
<head>
<meta charset="utf-8">
<title>Korvane — Web Design &amp; Development</title>
<link href="https://fonts.googleapis.com/css2?family=Noto+Sans+JP:wght@300;400;500&family=Lato:wght@300;400&display=swap" rel="stylesheet">
<style>
:root{
  --ink:#333;
  --sub:#777;
  --faint:#aaa;
  --line:#d6d6d6;
  --band:#efefef;
  --footer:#e9e9e9;
  --white:#fff;
  --navy:#405080;
  --blue:#4a86c5;
  --blue-soft:#7fb0df;
}
*{margin:0;padding:0;box-sizing:border-box}
html,body{width:1200px;height:3156px;overflow:hidden;background:var(--white)}
body{position:relative;font-family:"Noto Sans JP",sans-serif;color:var(--ink);font-size:14px}
.abs{position:absolute}
.en{font-family:"Lato",sans-serif;letter-spacing:.15em}

/* header */
.header{left:0;top:0;width:1200px;height:56px;background:var(--white);border-bottom:1px solid var(--line)}
.nav{top:18px;font-size:12px;color:var(--sub)}
.nav span{margin-right:42px}
.nav-left{left:180px}
.nav-right{left:700px}
.brand{left:540px;top:6px;width:120px;text-align:center}
.brand-mark{display:block;width:14px;height:14px;border:1.5px solid var(--ink);border-radius:50%;margin:0 auto 3px}
.brand-name{font-size:14px;font-family:"Lato",sans-serif;letter-spacing:.1em;color:var(--ink)}

/* hero */
.hero-bg{left:0;top:56px;width:1200px;height:544px;background:linear-gradient(#fafafa,#f1f1f1)}
.hero-photo{left:0;top:56px;width:560px;height:544px;background:linear-gradient(110deg,#e6e8ec 0%,#cfd3da 45%,#f4f4f4 100%)}
.service-box{left:672px;width:496px;background:rgba(255,255,255,.92);border:1px solid var(--line);padding:18px 24px}
.service-box h3{font-size:15px;font-weight:400;letter-spacing:.15em;border-bottom:1px solid var(--line);padding-bottom:8px;margin-bottom:12px}
.service-box p{font-size:11px;line-height:2;color:var(--sub)}
.service-box .btns{position:absolute;right:24px;bottom:16px;display:flex;gap:16px}
.btn{display:inline-block;border:1px solid var(--line);font-size:11px;padding:4px 18px;color:var(--sub);background:var(--white)}
.box-system{top:88px;height:212px}
.box-web{top:336px;height:204px}

/* intro */
.intro{left:240px;top:612px;width:760px}
.intro h2{font-size:18px;font-weight:400;letter-spacing:.2em;margin-bottom:18px}
.intro p{font-size:12px;line-height:2.1;color:var(--sub)}

/* section headings */
.sec-head{left:160px;width:880px;height:20px}
.sec-head .rule{position:absolute;left:0;right:0;top:10px;border-top:1px solid var(--line)}
.sec-head .tag{position:absolute;top:2px;font-size:11px;color:var(--faint);background:var(--white);padding:0 10px}
.sec-head .title{position:absolute;left:50%;transform:translateX(-50%);top:-8px;font-size:26px;color:var(--sub);background:var(--white);padding:0 24px;font-weight:300}
.sec-head .tag.l{left:160px}
.sec-head .tag.r{right:160px}

/* system band */
.band{left:0;width:1200px;background:var(--band)}
.system-band{top:1080px;height:300px}
.card{top:1148px;width:160px;text-align:center}
.card .thumb{width:160px;height:140px;background:var(--white);border:1px solid var(--line);padding:10px}
.card .thumb div{width:100%;height:100%}
.card p{font-size:10px;line-height:1.7;color:var(--sub);margin-top:8px}
.arrow{top:1210px}

/* design band */
.design-band{top:1580px;height:460px}
.shot{background:var(--white);border:1px solid var(--line)}

.case{left:0;width:1200px;top:2076px;text-align:center}
.case h4{font-size:17px;font-weight:500;letter-spacing:.08em}
.case a{display:block;font-size:11px;color:var(--blue);margin-top:10px;text-decoration:none}
.tabs{left:360px;top:2184px;font-size:11px;color:var(--faint)}
.tabs span{display:inline-block;margin-right:64px;padding-bottom:4px}

/* news */
.news{left:160px;top:2320px;width:880px;height:360px;background:var(--band);border-radius:6px}
.news h2{position:absolute;left:0;right:0;top:36px;text-align:center;font-size:22px;font-weight:300;color:var(--sub)}
.news h2::after{content:"";display:block;width:180px;border-top:1px solid var(--line);margin:10px auto 0}
.news ul{position:absolute;left:20px;top:108px;list-style:none}
.news li{font-size:12px;line-height:26px;color:var(--sub)}
.news li time{margin-right:10px}
.news .btn{position:absolute;right:80px;bottom:24px;padding:6px 48px}

/* contact banner */
.contact{left:172px;top:2752px;width:860px;height:112px;display:flex;border:1px solid var(--line)}
.contact .left{width:280px;background:var(--white);display:flex;flex-direction:column;align-items:center;justify-content:center;gap:4px}
.contact .right{flex:1;background:linear-gradient(90deg,var(--blue-soft),var(--blue));display:flex;align-items:center;justify-content:center;color:var(--white);font-size:26px;letter-spacing:.12em;font-weight:300}

/* footer */
.footer{left:0;top:2960px;width:1200px;height:196px;background:var(--footer)}
.fmenu{left:0;width:1200px;text-align:center;font-size:11px;color:var(--sub)}
.fmenu span{margin:0 22px}
.copy{left:0;top:3100px;width:1200px;text-align:center;font-size:10px;color:var(--faint)}
</style>
</head>
<body>

<header class="abs header">
  <nav class="abs nav nav-left en"><span>TOP</span><span>WEBDESIGN</span><span>DEVELOPMENT</span></nav>
  <div class="abs brand"><span class="brand-mark"></span><span class="brand-name">Korvane</span></div>
  <nav class="abs nav nav-right en"><span>PRICE</span><span>COMPANY</span><span>CONTACT</span></nav>
</header>

<div class="abs hero-bg"></div>
<div class="abs hero-photo" role="img" aria-label="スーツ姿の男性がノートパソコンの前で微笑んでいる写真"></div>

<section class="abs service-box box-system">
  <h3>システム開発</h3>
  <p>ご要望に合わせた業務システムを一から設計・開発いたします。<br>運用後の保守・改善まで継続してサポートいたします。</p>
  <p>小規模から大規模まで、柔軟な体制でお客様のビジネスを<br>支える最適なシステムをご提案いたします。</p>
  <div class="btns"><span class="btn">詳細</span><span class="btn">事例を見る</span></div>
</section>

<section class="abs service-box box-web">
  <h3>ホームページ制作</h3>
  <p>集客につながるホームページを企画から制作まで一貫して対応いたします。<br>スマートフォン対応や更新しやすい仕組みもご用意いたします。<br>目的に合わせたデザインで、御社の魅力を伝えます。</p>
  <div class="btns"><span class="btn">詳細</span><span class="btn">パック一覧</span></div>
</section>

<section class="abs intro">
  <h2>モノ作りを楽しむ</h2>
  <p>1998年の創業から ふたりのエンジニアが中心となり、システム開発とホームページ制作を行っております。<br>
  クライアント様から「ありがとう」の一言を頂戴できるよう、丁寧なヒアリングと確かな技術でお応えいたします。<br>
  お客様の笑顔と私たちの誠実さ、その信頼関係を大切に、これからもモノ作りを楽しんでまいります。</p>
</section>

<div class="abs sec-head" style="top:950px">
  <div class="rule"></div><span class="tag l en">WORKS</span><span class="title en">SYSTEM</span><span class="tag r en">DETAIL</span>
</div>

<div class="abs band system-band"></div>
<svg class="abs arrow" style="left:22px" width="16" height="24" viewBox="0 0 16 24"><path d="M12 2 2 12l10 10" fill="none" stroke="#999" stroke-width="2"/></svg>
<svg class="abs arrow" style="left:1162px" width="16" height="24" viewBox="0 0 16 24"><path d="M4 2l10 10-10 10" fill="none" stroke="#999" stroke-width="2"/></svg>

<div class="abs card" style="left:124px"><div class="thumb"><div role="img" aria-label="サーバー機器の写真" style="background:linear-gradient(#8fa3bf,#3b4a66)"></div></div><p>既存サーバー<br>リプレイスシステム</p></div>
<div class="abs card" style="left:324px"><div class="thumb"><div role="img" aria-label="管理画面のスクリーンショット" style="background:linear-gradient(#3a3f4a,#c5c9d2)"></div></div><p>ウェブ会員管理システム<br>顧客情報のアップデート</p></div>
<div class="abs card" style="left:520px;width:168px"><div class="thumb" style="width:168px;height:156px"><div role="img" aria-label="業務システム画面のスクリーンショット" style="background:linear-gradient(#f2e8d0,#c9b58a)"></div></div><p>在庫管理システム<br>受注管理・出荷処理</p></div>
<div class="abs card" style="left:724px"><div class="thumb"><div role="img" aria-label="予約システムの画面" style="background:linear-gradient(#6b5aa8,#c7bce6)"></div></div><p>予約管理システム<br>オンライン予約受付</p></div>
<div class="abs card" style="left:920px"><div class="thumb"><div role="img" aria-label="メール配信を表す封筒のイラスト" style="background:linear-gradient(#f4f4f4,#d9d9d9)"></div></div><p>メール配信システム<br>ステップメール機能</p></div>

<div class="abs sec-head" style="top:1478px">
  <div class="rule"></div><span class="tag l en">WORKS</span><span class="title en">DESIGN</span><span class="tag r en">DETAIL</span>
</div>

<div class="abs band design-band"></div>
<svg class="abs" style="left:22px;top:1628px" width="16" height="24" viewBox="0 0 16 24"><path d="M12 2 2 12l10 10" fill="none" stroke="#999" stroke-width="2"/></svg>
<svg class="abs" style="left:1162px;top:1628px" width="16" height="24" viewBox="0 0 16 24"><path d="M4 2l10 10-10 10" fill="none" stroke="#999" stroke-width="2"/></svg>

<div class="abs shot" style="left:160px;top:1700px;width:180px;height:300px" role="img" aria-label="制作事例サイトのスクリーンショット（白基調）"><div style="margin:10px;height:280px;background:linear-gradient(#f6f6f6 0%,#e4dcd6 40%,#fafafa 100%)"></div></div>
<div class="abs shot" style="left:860px;top:1700px;width:180px;height:300px" role="img" aria-label="制作事例サイトのスクリーンショット（黒基調）"><div style="margin:10px;height:280px;background:linear-gradient(#1a1a1a,#555)"></div></div>
<div class="abs shot" style="left:320px;top:1664px;width:560px;height:352px;box-shadow:0 4px 16px rgba(0,0,0,.15)" role="img" aria-label="株式会社ノルディアのホームページのスクリーンショット"><div style="height:24px;background:#e6e6e6;border-bottom:1px solid var(--line)"></div><div style="margin:14px;height:300px;background:linear-gradient(160deg,#e8f0f8 0%,#ffffff 45%,#cfdbe8 100%)"></div></div>

<section class="abs case">
  <h4>株式会社ノルディア ホームページ</h4>
  <a>https://nordia-sample.jp/</a>
</section>
<div class="abs tabs en"><span>WORKS</span><span>DESIGN</span><span>CODING</span><span>SYSTEM</span></div>

<section class="abs news">
  <h2 class="en">NEWS</h2>
  <ul>
    <li><time>2016/12/20</time>… 年末年始営業日 12月29日まで、年明けは1月5日から営業いたします</li>
    <li><time>2015/12/20</time>… 年末年始営業日 12月28日まで、年明けは1月5日から営業いたします</li>
    <li><time>2014/12/20</time>… 年末年始営業日 12月26日まで、年明けは1月6日から営業いたします</li>
    <li><time>2014/10/20</time>… ホームページのデザインを刷新いたしました</li>
    <li><time>2014/05/01</time>… プログラマー・デザイナーの新規募集を開始いたしました</li>
    <li><time>2014/01/01</time>… ホームページを公開いたしました</li>
  </ul>
  <span class="btn">一覧</span>
</section>

<aside class="abs contact">
  <div class="left"><span class="brand-mark"></span><span class="brand-name">Korvane</span></div>
  <div class="right">お問い合わせはこちら</div>
</aside>

<footer class="abs footer"></footer>
<div class="abs fmenu" style="top:3004px"><span>トップ</span><span>料金表</span><span>会社概要</span><span>お問い合わせ</span><span>ログイン</span></div>
<div class="abs fmenu" style="top:3040px"><span>ホームページ制作</span><span>業務システム開発</span></div>
<div class="abs copy en">Copyright © 1998-2017 Korvane Inc. All Rights Reserved.</div>

</body>
</html>
```